Steady Harvest of Patrons Programme Graphic

Please refer to attached graphic.
I wish to redesign this graphic to represent a programme of work that we (Brinvo) deliver to our customers.
The design represents 9 steps ( 3 steps at each of 3 levels) and is all about implementing the 'Steady Harvest of Patrons'

I like the fact that the increasing business growth is evident when you are progressing through the stages, but the current graphic looks dated and the colours are not working.
I would also like to incorporate the SHP logo we have created.

Target Market(s)

IT Sector - businesses looking to grow

Industry/Entity Type

We are a digital marketing company

Requirements
Must have
• Clear, concise design
Should not have
• Design must not be complicated

```html
<!DOCTYPE html>
<html lang="en">
<head>
<meta charset="utf-8">
<title>Steady Harvest of Patrons – Programme Graphic</title>
<link rel="stylesheet" href="https://fonts.googleapis.com/css2?family=Oswald:wght@500;600&family=Montserrat:wght@700;800&display=swap">
<style>
  :root {
    --navy: #232356;
    --navy-deep: #1d1f4f;
    --royal: #1456b4;
    --cyan: #1496d4;
    --sky: #3fc4ef;
    --slate: #7592c6;
    --band: #2c2f7e;
    --white: #ffffff;
    --bg-top: #ffffff;
    --bg-bottom: #e3e4e8;
  }
  html, body {
    margin: 0;
    padding: 0;
    width: 1200px;
    height: 849px;
    overflow: hidden;
    background: var(--bg-top);
  }
  .programme-graphic {
    display: block;
    width: 1200px;
    height: 849px;
  }
  .step-number { font-family: "Montserrat", sans-serif; font-weight: 800; font-size: 52px; fill: var(--white); }
  .stage-label { font-family: "Montserrat", sans-serif; font-weight: 800; font-size: 24px; fill: var(--white); letter-spacing: 1px; }
  .step-item { font-family: "Oswald", sans-serif; font-weight: 500; font-size: 29px; fill: var(--white); }
  .cadence-title { font-family: "Oswald", sans-serif; font-weight: 500; font-size: 21px; fill: var(--white); }
  .cadence-sub { font-family: "Montserrat", sans-serif; font-weight: 700; font-size: 10.5px; fill: var(--white); letter-spacing: .3px; }
  .programme-title { font-family: "Oswald", sans-serif; font-weight: 600; font-size: 46px; fill: var(--white); }
  .brand-name { font-family: "Oswald", sans-serif; font-weight: 600; font-size: 34px; fill: var(--sky); }
  .mark-label { font-family: "Oswald", sans-serif; font-weight: 600; font-size: 15px; fill: var(--sky); }
  .icon-line { fill: none; stroke: var(--white); stroke-width: 2; stroke-linecap: round; stroke-linejoin: round; }
  .icon-fill { fill: var(--white); }
</style>
</head>
<body>
<svg class="programme-graphic" viewBox="0 0 1200 849" xmlns="http://www.w3.org/2000/svg" aria-labelledby="graphic-title">
  <title id="graphic-title">Steady Harvest of Patrons: three stages, nine steps</title>
  <defs>
    <linearGradient id="bgGrad" x1="0" y1="0" x2="0" y2="1">
      <stop offset="0" stop-color="var(--bg-top)"/>
      <stop offset="1" stop-color="var(--bg-bottom)"/>
    </linearGradient>
    <linearGradient id="columnGrad" x1="0" y1="0" x2="0" y2="1">
      <stop offset="0" stop-color="#1660c2"/>
      <stop offset=".55" stop-color="#1a3f96"/>
      <stop offset="1" stop-color="var(--navy)"/>
    </linearGradient>
    <linearGradient id="floorGrad" x1="0" y1="0" x2="0" y2="1">
      <stop offset="0" stop-color="#1aa3dc"/>
      <stop offset="1" stop-color="#56d2f2"/>
    </linearGradient>
    <linearGradient id="arrowBackGrad" x1="1" y1="0" x2="0" y2="0">
      <stop offset="0" stop-color="#c9e6f7" stop-opacity=".3"/>
      <stop offset="1" stop-color="#1fa2dc"/>
    </linearGradient>
    <linearGradient id="arrowFrontGrad" x1="0" y1="0" x2="1" y2="0">
      <stop offset="0" stop-color="#cfe9f8" stop-opacity=".25"/>
      <stop offset="1" stop-color="#1fb0e6"/>
    </linearGradient>
  </defs>

  <rect class="background" width="1200" height="849" fill="url(#bgGrad)"/>
  <polygon class="floor" points="178,789 1023,789 1200,849 0,849" fill="url(#floorGrad)"/>

  <!-- rear sweeping arrow -->
  <g class="arrow-back">
    <path d="M1000 78 C 700 110, 400 220, 185 345" fill="none" stroke="url(#arrowBackGrad)" stroke-width="16"/>
    <polygon points="137,390 186,320 200,365" fill="#2aaee4"/>
  </g>

  <!-- stage columns -->
  <g class="stage stage-1">
    <polygon class="column" points="219,407 438,335 438,640 219,640" fill="url(#columnGrad)"/>
    <polygon class="ribbon" points="219,373 438,294 438,335 219,407" fill="var(--cyan)"/>
    <polygon points="219,402 438,330 438,335 219,407" fill="var(--navy-deep)"/>
    <polygon class="flag" points="219,267 356,316 219,369" fill="var(--navy)"/>
    <text class="step-number" x="229" y="338">1</text>
    <text class="stage-label" transform="translate(264 381) rotate(-19.8)">RHYTHMIC</text>
  </g>

  <g class="stage stage-2">
    <polygon class="column" points="492,315 712,243 712,640 492,640" fill="url(#columnGrad)"/>
    <polygon class="ribbon" points="492,270 712,198 712,243 492,315" fill="var(--slate)"/>
    <polygon points="492,310 712,238 712,243 492,315" fill="var(--navy-deep)"/>
    <polygon class="flag" points="492,174 628,222 492,270" fill="var(--cyan)"/>
    <text class="step-number" x="506" y="243">2</text>
    <text class="stage-label" transform="translate(533 287) rotate(-19.8)">ACQUISITION</text>
  </g>

  <g class="stage stage-3">
    <polygon class="column" points="765,215 984,144 984,640 765,640" fill="url(#columnGrad)"/>
    <polygon class="ribbon" points="765,168 984,99 984,144 765,215" fill="var(--navy)"/>
    <polygon class="flag" points="765,89 881,127 765,168" fill="var(--royal)"/>
    <text class="step-number" x="772" y="148">3</text>
    <text class="stage-label" transform="translate(800 190) rotate(-19.8)">CUSTOMERS</text>
  </g>

  <!-- front sweeping arrow -->
  <g class="arrow-front">
    <path d="M219 424 C 500 400, 800 290, 1030 148" fill="none" stroke="url(#arrowFrontGrad)" stroke-width="16" opacity=".85"/>
    <polygon points="1067,115 992,141 1019,153 1018,185" fill="#2ab3e7"/>
  </g>

  <!-- step items: stage 1 -->
  <g class="step-list">
    <g class="step">
      <polygon points="212,470 256,470 263,486 256,502 212,502" fill="var(--cyan)"/>
      <circle class="icon-fill" cx="227" cy="480" r="4"/><circle class="icon-fill" cx="240" cy="479" r="4.5"/><circle class="icon-fill" cx="252" cy="480" r="4"/>
      <path class="icon-fill" d="M220 495 q7-10 14 0z M233 495 q7-11 14 0z M245 495 q7-10 14 0z"/>
      <text class="step-item" x="270" y="498">PERSONAS</text>
    </g>
    <g class="step">
      <polygon points="212,526 256,526 263,542 256,558 212,558" fill="var(--cyan)"/>
      <ellipse class="icon-fill" cx="236" cy="533" rx="9" ry="3.5"/>
      <rect class="icon-fill" x="227" y="537" width="18" height="5" rx="2"/>
      <rect class="icon-fill" x="227" y="544" width="18" height="5" rx="2"/>
      <rect class="icon-fill" x="227" y="551" width="18" height="4" rx="2"/>
      <text class="step-item" x="268" y="553">DATABASE</text>
    </g>
    <g class="step">
      <polygon points="212,584 256,584 263,600 256,616 212,616" fill="var(--cyan)"/>
      <circle class="icon-line" cx="236" cy="600" r="9" stroke-dasharray="4 2.5" stroke-width="3"/>
      <circle class="icon-line" cx="236" cy="600" r="4"/>
      <text class="step-item" x="266" y="611">SYSTEMS</text>
    </g>
  </g>

  <!-- step items: stage 2 -->
  <g class="step-list">
    <g class="step">
      <polygon points="486,470 530,470 537,486 530,502 486,502" fill="#3a72c4"/>
      <path class="icon-fill" d="M497 475 h22 v15 h-9 l-4 5 v-5 h-9z"/>
      <circle cx="503" cy="483" r="1.4" fill="#3a72c4"/><circle cx="508" cy="483" r="1.4" fill="#3a72c4"/><circle cx="513" cy="483" r="1.4" fill="#3a72c4"/>
      <text class="step-item" x="550" y="496">MESSAGING</text>
    </g>
    <g class="step">
      <polygon points="486,526 530,526 537,542 530,558 486,558" fill="#3a72c4"/>
      <circle class="icon-line" cx="508" cy="542" r="10" stroke-dasharray="5 2"/>
      <path class="icon-line" d="M503 542 l4 4 l7 -8"/>
      <text class="step-item" x="550" y="554">LEADS</text>
    </g>
    <g class="step">
      <polygon points="486,584 530,584 537,600 530,616 486,616" fill="#3a72c4"/>
      <path class="icon-line" stroke-width="3.5" d="M500 592 h14 q3 0 3 4 q0 4 -3 4 h-8 q-3 0 -3 4 q0 4 3 4 h12"/>
      <text class="step-item" x="550" y="611">PIPELINE</text>
    </g>
  </g>

  <!-- step items: stage 3 -->
  <g class="step-list">
    <g class="step">
      <polygon points="758,468 802,468 809,484 802,500 758,500" fill="var(--royal)"/>
      <path class="icon-line" d="M769 491 l7-7 l5 4 l9-9 M784 479 h6 v6"/>
      <text class="step-item" x="823" y="495">SALES</text>
    </g>
    <g class="step">
      <polygon points="758,526 802,526 809,542 802,558 758,558" fill="var(--royal)"/>
      <path class="icon-fill" d="M772 548 h16 l-2 7 h-12z"/>
      <path class="icon-line" d="M780 548 v-10"/>
      <path class="icon-fill" d="M780 538 q-8 0 -8 -7 q8 0 8 7z M780 536 q1 -8 9 -8 q0 8 -9 8z"/>
      <text class="step-item" x="823" y="553">NURTURE</text>
    </g>
    <g class="step">
      <polygon points="758,584 802,584 809,600 802,616 758,616" fill="var(--royal)"/>
      <path class="icon-line" d="M772 590 h10 l6 6 v15 h-16z M782 590 v6 h6"/>
      <path class="icon-line" d="M776 603 h8 M781 600 l3 3 l-3 3"/>
      <text class="step-item" x="823" y="611">REFERENCE</text>
    </g>
  </g>

  <!-- cadence bases -->
  <g class="cadence">
    <polygon points="216,640 438,640 445,646 209,646" fill="#1a86c4"/>
    <rect x="209" y="646" width="236" height="53" fill="var(--cyan)"/>
    <text class="cadence-title" x="327" y="673" text-anchor="middle">NUMBERS THAT MATTER</text>
    <text class="cadence-sub" x="323" y="689" text-anchor="middle">FOUNDATION METRICS</text>
  </g>
  <g class="cadence">
    <polygon points="489,640 712,640 718,646 483,646" fill="#1a86c4"/>
    <rect x="483" y="646" width="235" height="53" fill="var(--cyan)"/>
    <text class="cadence-title" x="593" y="673" text-anchor="middle">WEEKLY SCORECARD</text>
    <text class="cadence-sub" x="591" y="689" text-anchor="middle">TACTICAL EXECUTION</text>
  </g>
  <g class="cadence">
    <polygon points="762,640 984,640 991,646 756,646" fill="#1a86c4"/>
    <rect x="756" y="646" width="235" height="53" fill="var(--cyan)"/>
    <text class="cadence-title" x="871" y="671" text-anchor="middle">MONTHLY SCORECARD</text>
    <text class="cadence-sub" x="868" y="689" text-anchor="middle">STRATEGIC REVIEW</text>
  </g>

  <!-- platform -->
  <g class="platform">
    <polygon points="209,699 991,699 1023,715 178,715" fill="var(--band)"/>
    <rect x="178" y="715" width="845" height="74" fill="var(--navy)"/>
    <rect x="193" y="733" width="38" height="38" fill="none" stroke="var(--sky)" stroke-width="2.5"/>
    <text class="mark-label" x="212" y="758" text-anchor="middle">SHP</text>
    <text class="programme-title" x="262" y="773">STEADY HARVEST OF PATRONS</text>
    <text class="brand-name" x="1008" y="768" text-anchor="end">Brinvo</text>
  </g>
</svg>
</body>
</html>
```